Greek Yogurt Design

Design Brief – Premium Greek Yogurt Line (150g Pot)
Background
We are a small-to-medium dairy producer launching a new premium Greek yogurt range. This line will come in slightly larger pots than our standard yogurts, and we are targeting an upmarket clientele with a higher price point.
Product Details
Product: Greek Yogurt (fruit on the bottom, yogurt on top)
Flavours:
Natural
Strawberry
Forest Fruit
Peach & Apricot
Vanilla
Mango
Weight: 150g
Kosher Certification: 2 logos must be applied neatly (logos provided).
Lid: Standard universal lid (not flavour-specific).
Design Style
Clean, elegant, and premium feel (avoid clutter).
Should stand out as sophisticated compared to our standard range.
Visual hierarchy:
Brand & product type (Greek Yogurt) should be clear.
Flavour indicated with subtle but distinct cues (colour palette, fruit illustration/photography).
“Fruit on the bottom” message should be communicated simply.
Premium cues: minimalist typography, restrained colour palette, elegant fruit imagery.
References / Inspiration
Velmora Yogurt
– clean, bold, dairy-traditional.
Brask Dairy Greek Style
– natural, elegant design.
Lunaro Greek Yogurt
– modern, colourful yet clean.
Deliverables
Pot sleeve / pot design (to wrap around container).
Must work across all flavours with colour/flavour variation.
Space for universal lid (do not design individual lids).
Application of 2 kosher logos in a balanced way.
Updates
Industry/Entity Type
Dairy
Colors
Designer to choose colors to be used in the design.
Look and feel
Each slider illustrates characteristics of the customer's brand and the style your logo design should communicate.

```html
<!DOCTYPE html>
<html lang="en">
<head>
<meta charset="utf-8">
<title>Milvaro Greek Yogurt – Strawberry Pot</title>
<link href="https://fonts.googleapis.com/css2?family=Lilita+One&family=Baloo+2:wght@700&family=Roboto+Condensed:wght@400;700&display=swap" rel="stylesheet">
<style>
  :root {
    --backdrop: #72566b;
    --magenta: #a3236f;
    --magenta-deep: #6e1453;
    --magenta-light: #c94a98;
    --pink-band: #e6a3cd;
    --leaf-green: #5cb84a;
    --leaf-dark: #3f8f35;
    --cream: #ffffff;
    --ink: #1a1a1a;
    --yogurt-blue: #2a6fc9;
    --berry: #e0443f;
    --badge: #f3ecef;
  }
  html, body {
    margin: 0;
    padding: 0;
    width: 1200px;
    height: 900px;
    overflow: hidden;
    background: var(--backdrop);
  }
  .artboard { display: block; width: 1200px; height: 900px; }
  .brand-name { font-family: "Baloo 2", sans-serif; font-weight: 700; fill: var(--leaf-green); }
  .brand-name--light { fill: var(--cream); }
  .product-greek { font-family: "Lilita One", sans-serif; fill: var(--cream); stroke: var(--yogurt-blue); stroke-width: 3; paint-order: stroke; }
  .product-yogurt { font-family: "Lilita One", sans-serif; fill: var(--yogurt-blue); letter-spacing: 4px; }
  .flavour-note { font-family: "Roboto Condensed", sans-serif; font-weight: 400; fill: var(--cream); letter-spacing: 3px; }
  .claim { font-family: "Roboto Condensed", sans-serif; font-weight: 700; fill: var(--ink); }
  .claim--light { fill: var(--cream); }
  .weight { font-family: "Roboto Condensed", sans-serif; font-weight: 700; fill: var(--cream); letter-spacing: 1px; }
  .kosher-badge { fill: var(--badge); stroke: var(--leaf-dark); stroke-width: 2; }
</style>
</head>
<body>
<svg class="artboard" viewBox="0 0 1200 900" xmlns="http://www.w3.org/2000/svg">
  <defs>
    <linearGradient id="sleeveGradient" x1="0" x2="1" y1="0" y2="0">
      <stop offset="0" stop-color="var(--magenta-deep)"/>
      <stop offset="0.5" stop-color="var(--magenta-light)"/>
      <stop offset="1" stop-color="var(--magenta-deep)"/>
    </linearGradient>
    <radialGradient id="berryGradient" cx="0.5" cy="0.5" r="0.6">
      <stop offset="0" stop-color="#f6b9a8"/>
      <stop offset="0.55" stop-color="var(--berry)"/>
      <stop offset="1" stop-color="#f3f0ee"/>
    </radialGradient>
    <clipPath id="potFrontBody"><polygon points="410,240 710,240 685,690 435,690"/></clipPath>
    <clipPath id="potBackBody"><polygon points="760,240 1060,240 1035,690 785,690"/></clipPath>
    <clipPath id="lidFace"><circle cx="230" cy="450" r="150"/></clipPath>
  </defs>

  <!-- Universal lid (same for every flavour) -->
  <g class="lid">
    <path d="M95 520 L60 560 Q70 580 95 565 Z" fill="var(--pink-band)"/>
    <g clip-path="url(#lidFace)">
      <rect x="80" y="300" width="300" height="300" fill="var(--magenta)"/>
      <rect x="80" y="300" width="300" height="95" fill="var(--leaf-green)"/>
      <rect x="80" y="470" width="300" height="36" fill="var(--pink-band)"/>
    </g>
    <circle cx="230" cy="450" r="150" fill="none" stroke="var(--magenta-deep)" stroke-width="4"/>
    <text class="brand-name brand-name--light" x="230" y="358" font-size="34" text-anchor="middle">Milvaro</text>
    <text class="product-greek" x="230" y="462" font-size="58" text-anchor="middle">GREEK</text>
    <text class="product-yogurt" x="232" y="498" font-size="26" text-anchor="middle">YOGURT</text>
    <text class="claim claim--light" x="230" y="540" font-size="18" text-anchor="middle">Fruit on the bottom</text>
  </g>

  <!-- Pot front -->
  <g class="pot pot--front">
    <g clip-path="url(#potFrontBody)">
      <rect x="400" y="240" width="320" height="460" fill="url(#sleeveGradient)"/>
      <rect x="400" y="480" width="320" height="40" fill="var(--pink-band)"/>
      <rect x="400" y="540" width="320" height="18" fill="var(--leaf-green)"/>
      <rect x="400" y="558" width="320" height="12" fill="var(--cream)"/>
      <rect x="400" y="570" width="320" height="14" fill="var(--leaf-dark)"/>
      <rect x="400" y="584" width="320" height="40" fill="var(--cream)"/>
      <rect x="400" y="624" width="320" height="18" fill="var(--leaf-green)"/>
      <rect x="400" y="642" width="320" height="14" fill="var(--cream)"/>
      <rect x="400" y="656" width="320" height="40" fill="var(--leaf-green)"/>
    </g>
    <rect x="398" y="218" width="324" height="26" rx="6" fill="var(--magenta-light)"/>
    <text class="brand-name" x="560" y="330" font-size="44" text-anchor="middle">Milvaro</text>
    <text class="flavour-note" x="560" y="372" font-size="20" text-anchor="middle">STRAWBERRY</text>
    <text class="product-greek" x="560" y="470" font-size="86" text-anchor="middle">GREEK</text>
    <text class="product-yogurt" x="560" y="514" font-size="40" text-anchor="middle">YOGURT</text>
    <text class="claim" x="560" y="612" font-size="24" text-anchor="middle">Fruit on the bottom</text>
    <text class="weight" x="560" y="681" font-size="20" text-anchor="middle">150g</text>
  </g>

  <!-- Pot back -->
  <g class="pot pot--back">
    <g clip-path="url(#potBackBody)">
      <rect x="750" y="240" width="320" height="460" fill="url(#sleeveGradient)"/>
      <rect x="750" y="540" width="320" height="18" fill="var(--leaf-green)"/>
      <rect x="750" y="558" width="320" height="12" fill="var(--cream)"/>
      <rect x="750" y="570" width="320" height="14" fill="var(--leaf-dark)"/>
      <rect x="750" y="584" width="320" height="40" fill="var(--cream)"/>
      <rect x="750" y="624" width="320" height="18" fill="var(--leaf-green)"/>
      <rect x="750" y="642" width="320" height="14" fill="var(--cream)"/>
      <rect x="750" y="656" width="320" height="40" fill="var(--leaf-green)"/>
    </g>
    <rect x="748" y="218" width="324" height="26" rx="6" fill="var(--magenta-light)"/>
    <ellipse cx="910" cy="430" rx="125" ry="90" fill="url(#berryGradient)" role="img" aria-label="Ripe strawberries splashing into creamy yogurt"/>
    <g class="kosher-badges">
      <circle class="kosher-badge" cx="885" cy="604" r="15"/>
      <circle class="kosher-badge" cx="935" cy="604" r="15"/>
    </g>
    <text class="weight" x="910" y="681" font-size="20" text-anchor="middle">150g</text>
  </g>
</svg>
</body>
</html>
```